Stylish Business Card for Modern hair salon

I need a simple business card design using our salon logo and colours that are in the logo. We service clients of all ages but predominantly those in the 18 to 55 age range. We have a young staff and are looking to have a card that will present a modern and clean image that represents who we are. The card should be in black and white same as our logo. Minimal use of other colours is allowed.

Industry/Entity Type

Hair And Beauty

Contact Information for Business Card

The design should have the following information
salon name - TR Hair Studio
address - 2751 Birchfield Rd.E. Mississauga, ON L7P3K2
phone - 905 614-2870
website - trhairexample.ca
instagram - tr.hairstudio
twitter - @TR_HairStudio

Colors
000000
ffffff
474747

Requirements
Must have
• simple design, salon name, address, phone, website, instagram, twitter info
• Back of card should have the following:
• YOUR NEXT APPOINTMENT
• DATE
• TIME
Nice to have
• simple design, clear to see and read,
• predominantly black and white colour, minimal use of other colours is ok
Should not have
• many colours, various fonts

```html
<!DOCTYPE html>
<html lang="en">
<head>
<meta charset="utf-8">
<title>TR Hair Studio – Business Card</title>
<link href="https://fonts.googleapis.com/css2?family=Mulish:ital,wght@0,400;0,700;1,400&display=swap" rel="stylesheet">
<style>
  :root {
    --ink: #000000;
    --paper: #ffffff;
    --grey: #474747;
    --rule: #6b6b6b;
    --frame: #9a9a9a;
  }
  html, body {
    margin: 0;
    padding: 0;
    width: 1200px;
    height: 1200px;
    overflow: hidden;
    background: var(--paper);
    font-family: "Mulish", sans-serif;
  }
  .canvas {
    position: relative;
    width: 1200px;
    height: 1200px;
  }
  .card {
    position: absolute;
    left: 250px;
    width: 700px;
    height: 400px;
    box-sizing: border-box;
  }
  .card-front {
    top: 162px;
    background: var(--ink);
    color: var(--paper);
  }
  .card-back {
    top: 640px;
    background: var(--paper);
    border: 1px solid var(--frame);
    color: var(--ink);
  }
  .divider {
    position: absolute;
    width: 2px;
    background: var(--rule);
  }
  .card-front .divider { left: 381px; top: 64px; height: 277px; }
  .card-back .divider { left: 284px; top: 60px; height: 277px; background: var(--grey); }

  .wordmark {
    position: absolute;
    font-weight: 400;
    letter-spacing: 0.06em;
    line-height: 1;
    white-space: nowrap;
    text-transform: uppercase;
    transform: translate(-50%, -50%);
  }
  .card-front .wordmark { left: 196px; top: 190px; font-size: 27px; color: var(--paper); }
  .card-back .wordmark { left: 151px; top: 192px; font-size: 34px; color: var(--ink); }

  .contact {
    position: absolute;
    left: 406px;
    top: 0;
    font-size: 16px;
    line-height: 1;
    color: var(--paper);
  }
  .contact p { position: absolute; margin: 0; white-space: nowrap; }
  .contact .salon-name { top: 114px; font-size: 29px; letter-spacing: 0.02em; }
  .contact .addr-1 { top: 163px; }
  .contact .addr-2 { top: 182px; }
  .contact .phone { top: 219px; }
  .contact .web { top: 255px; }
  .contact .insta { top: 276px; }
  .contact .twitter { top: 298px; }
  .contact em { font-style: italic; }

  .appointment {
    position: absolute;
    left: 349px;
    top: 0;
    line-height: 1;
  }
  .appointment p { position: absolute; margin: 0; white-space: nowrap; }
  .appointment .kicker { top: 97px; font-size: 21px; }
  .appointment .title { top: 125px; font-size: 29px; font-weight: 700; color: var(--grey); letter-spacing: 0.02em; }
  .appointment .field { font-size: 21px; }
  .appointment .date { top: 220px; }
  .appointment .time { top: 288px; }
  .fill-line {
    position: absolute;
    left: 70px;
    width: 204px;
    height: 1px;
    background: var(--ink);
  }
  .fill-line.date-line { top: 237px; }
  .fill-line.time-line { top: 306px; }
</style>
</head>
<body>
<div class="canvas">
  <section class="card card-front" aria-label="Card front">
    <div class="wordmark">TR Hair Studio</div>
    <div class="divider"></div>
    <div class="contact">
      <p class="salon-name">TR HAIR STUDIO</p>
      <p class="addr-1">2751 Birchfield Rd.E.</p>
      <p class="addr-2">Mississauga, ON L7P3K2</p>
      <p class="phone">905 614-2870</p>
      <p class="web"><em>website:</em> trhairexample.ca</p>
      <p class="insta"><em>instagram:</em> tr.hairstudio</p>
      <p class="twitter"><em>twitter:</em> @TR_HairStudio</p>
    </div>
  </section>

  <section class="card card-back" aria-label="Card back">
    <div class="wordmark">TR Hair</div>
    <div class="divider"></div>
    <div class="appointment">
      <p class="kicker">YOUR NEXT</p>
      <p class="title">APPOINTMENT</p>
      <p class="field date">DATE:</p>
      <span class="fill-line date-line"></span>
      <p class="field time">TIME:</p>
      <span class="fill-line time-line"></span>
    </div>
  </section>
</div>
</body>
</html>
```